Web Design for Small Healthcare Startup

Hello,

We are seeking a Website Design for a healthcare company focusing on mobile vaccinations, employee health and wellness services onsite at businesses, and consulting services relating to Healthcare Entities in WA state. Our company’s mission is to “To aid in a healthier workplace”. Vitality Caravan will provide on-site wellness services to employers that simplify and streamline employee preventative health as well as onsite consulting services to help with compliance of Healthcare Entities.

We are seeking a Website Design for Vitality Caravan, PLLC. Our company’s mission is to provide mobile health and wellness services to employers onsite at their businesses. These services include mobile vaccinations clinics for employees as well as wellness and health screenings. The company will also offer healtcare compliance consulting services for Healthcare Entities. The company was founded to bring these important healthcare services to businesses and keep employees healthy. Healthy employees are the cornerstone to a great business and we want to help orginazations achieve their goals of having a healthy productive workforce.

We are looking for a moderin website design that will need to be coded. We have attached our current logo design for reference as well as a brief questionare regarding our business for your information (not necessary to include all information). We would like something SEO friendly and easy to navigate.

Thank you!

Vitality Caravan, PLLC

Target Market(s)

Small Businesses

Industry/Entity Type

Healthcare

Coding

Coded - Design and coding required

Number of Pages Required

1 page

Requirements
Nice to have
• SEO Friendly, Incorporate Logo

```html
<!DOCTYPE html>
<html lang="en">
<head>
<meta charset="utf-8">
<title>Vitality Caravan, PLLC – On-site Workplace Wellness</title>
<link href="https://fonts.googleapis.com/css2?family=Roboto:wght@400;500;700;900&display=swap" rel="stylesheet">
<style>
:root{
  --blue:#0d4fa8;
  --blue-dark:#083f8c;
  --purple:#a0479c;
  --ink:#1f1f1f;
  --text:#3a3a3a;
  --pale:#f2f6fc;
  --black:#000;
  --white:#fff;
}
*{box-sizing:border-box;margin:0;padding:0}
html,body{width:1200px;height:3393px;overflow:hidden}
body{position:relative;font-family:'Roboto',sans-serif;color:var(--text);background:var(--white)}
.abs{position:absolute}
a{color:inherit;text-decoration:none}

/* header */
.topline{left:0;top:0;width:1200px;height:4px;background:var(--blue)}
.site-header{left:0;top:4px;width:1200px;height:100px;background:var(--white)}
.brand{display:flex;align-items:center;gap:8px;font-weight:700;font-size:22px;color:var(--blue)}
.brand-mark{width:14px;height:14px;border-radius:50%;background:var(--purple)}
.header-brand{left:108px;top:38px}
.nav{left:0;top:46px;width:1200px;font-size:15px;color:#333;text-transform:uppercase}
.nav a{position:absolute;white-space:nowrap}
.nav .active{color:var(--purple)}
.nav-underline{left:364px;top:70px;width:44px;height:10px}
.search-btn{left:877px;top:33px;width:41px;height:41px;border-radius:50%;background:#eee;display:flex;align-items:center;justify-content:center}
.login-btn{left:965px;top:31px;width:123px;height:45px;border-radius:23px;background:var(--blue);color:#fff;font-weight:700;font-size:15px;display:flex;align-items:center;justify-content:center;gap:12px}

/* hero */
.hero-photo{left:0;top:104px;width:1200px;height:726px;background:linear-gradient(100deg,#e7dfd5 0%,#d9cdbf 35%,#cbbca9 60%,#b8a893 100%)}
.hero-title{left:520px;top:372px;width:594px;text-align:center;color:#fff;font-size:45px;font-weight:700;line-height:48px;text-shadow:0 2px 6px rgba(0,0,0,.35)}
.hero-sub{left:540px;top:486px;width:554px;text-align:center;color:#fff;font-size:15px;font-weight:500;line-height:26px;text-shadow:0 1px 4px rgba(0,0,0,.35)}
.btn{display:flex;align-items:center;justify-content:center;gap:10px;border-radius:26px;color:#fff;font-weight:700;font-size:15px;text-transform:uppercase}
.btn-purple{background:var(--purple)}
.btn-blue{background:var(--blue)}
.hero-btn{left:730px;top:558px;width:173px;height:50px}
.hero-edge{left:0;top:760px;width:1200px;height:72px}

/* section titles */
.section-title{left:0;width:1200px;text-align:center;font-size:35px;font-weight:700;color:var(--ink)}
.section-title span{color:var(--blue)}
.title-line{width:46px;height:10px}

/* services */
.service-card{top:1004px;height:313px;color:#fff}
.service-photo{width:100%;height:100%}
.service-icon{width:72px;height:72px;border-radius:50%;border:2px dashed rgba(255,255,255,.9);display:flex;align-items:center;justify-content:center}
.service-icon i{display:block;width:56px;height:56px;border-radius:50%;background:#fff}
.service-label{width:100%;text-align:center;font-size:17px;font-weight:700}
.service-featured{background:var(--blue);text-align:center}
.service-featured p{font-size:12.5px;line-height:21px;padding:0 22px}
.learn-small{background:#fff;color:var(--blue);border-radius:20px;font-size:12px;font-weight:700;height:38px;width:160px;display:flex;align-items:center;justify-content:center;gap:8px}
.arrow{font-size:22px;color:#222}

/* about */
.about-bg{left:0;top:1396px;width:1200px;height:635px;background:var(--pale)}
.about-title{left:110px;top:1496px;font-size:35px;font-weight:700;color:var(--ink)}
.about-title span{color:var(--blue)}
.about-text{left:110px;top:1580px;width:440px;font-size:15px;line-height:27.4px;text-align:justify;color:#444}
.dots{left:620px;top:1474px;width:96px;height:86px;background-image:radial-gradient(var(--blue) 1.6px,transparent 1.7px);background-size:10px 10px}
.about-accent{left:750px;top:1660px;width:350px;height:300px;background:var(--blue)}
.about-photo{left:643px;top:1490px;width:445px;height:457px;background:linear-gradient(135deg,#c9d3dc,#a3b3c2 50%,#7f8fa2)}

/* cta */
.cta{left:0;top:2031px;width:1200px;height:309px;background:var(--blue)}
.cta-title{left:0;top:2080px;width:1200px;text-align:center;color:#fff;font-size:41px;font-weight:700;line-height:47px}
.cta-btn{left:512px;top:2230px;width:175px;height:50px}

/* pricing */
.pricing-bg{left:0;top:2340px;width:1200px;height:640px;background:linear-gradient(180deg,#fff 0%,#f3f4f6 60%,#e9ebee 100%)}
.price-card{top:2521px;width:270px;height:355px;background:#fff;box-shadow:0 2px 10px rgba(0,0,0,.08);text-align:center}
.price-card.featured{border:1px solid var(--blue)}
.step{margin-top:30px;font-weight:700;font-size:17px;color:var(--ink)}
.step-icon{width:74px;height:66px;margin:20px auto 0;border-radius:8px;background:var(--blue)}
.step-desc{margin-top:20px;font-size:15px;line-height:20px;color:#333;padding:0 24px}
.step-rule{width:48px;height:2px;background:var(--blue);margin:14px auto 12px}
.ticks{list-style:none;text-align:left;padding-left:28px}
.ticks li{display:flex;align-items:center;gap:14px;font-size:15px;height:34px;color:#333}
.tick{width:12px;height:12px;flex:none}

/* footer */
.footer{left:0;top:2960px;width:1200px;height:433px;background:var(--black);color:#fff}
.footer-edge{left:0;top:2955px;width:1200px;height:82px}
.footer-brand{left:110px;top:3118px}
.footer-contact{left:110px;font-size:15px;display:flex;align-items:center;gap:12px}
.footer-head{font-size:19px;font-weight:700}
.footer-links{list-style:none;font-size:15px}
.footer-links li{height:34.3px}
.newsletter{left:792px;top:3151px;width:310px;font-size:15px;line-height:21px}
.subscribe{left:792px;top:3183px;width:297px;height:46px;background:#fff;border-radius:24px;display:flex;align-items:center;justify-content:space-between;padding-left:24px}
.subscribe span{color:#888;font-size:12px}
.subscribe b{background:var(--purple);height:46px;width:124px;border-radius:24px;display:flex;align-items:center;justify-content:center;font-size:17px}
.social{left:792px;top:3250px;display:flex;align-items:center;gap:10px;font-weight:700;font-size:15px}
.social i{display:block;width:11px;height:11px;border-radius:50%;background:#fff}
.footer-rule{left:110px;top:3330px;width:980px;height:1px;background:#333}
.copyright{left:0;top:3350px;width:1200px;text-align:center;font-size:13px}
</style>
</head>
<body>

<div class="abs topline"></div>
<header class="abs site-header"></header>
<a class="abs brand header-brand" href="#"><span class="brand-mark"></span>Vitality Caravan</a>
<nav class="abs nav">
  <a class="active" style="left:365px">Home</a>
  <a style="left:442px">About Us</a>
  <a style="left:549px">Services</a>
  <a style="left:653px">Pricing</a>
  <a style="left:747px">Contact Us</a>
</nav>
<svg class="abs nav-underline" viewBox="0 0 44 10"><circle cx="5" cy="5" r="3.5" fill="none" stroke="#0d4fa8" stroke-width="2"/><line x1="9" y1="5" x2="44" y2="5" stroke="#0d4fa8" stroke-width="2"/></svg>
<div class="abs search-btn"><svg width="14" height="14" viewBox="0 0 14 14"><circle cx="6" cy="6" r="4.5" fill="none" stroke="#222" stroke-width="2"/><line x1="9.5" y1="9.5" x2="13" y2="13" stroke="#222" stroke-width="2"/></svg></div>
<a class="abs login-btn" href="#">LOGIN <svg width="10" height="12" viewBox="0 0 10 12"><path d="M2 5V3.5a3 3 0 0 1 6 0V5" fill="none" stroke="#fff" stroke-width="1.6"/><rect x="0" y="5" width="10" height="7" rx="1" fill="#fff"/></svg></a>

<!-- hero -->
<div class="abs hero-photo" role="img" aria-label="Young woman stretching in a yoga pose on a mat in a bright living room with plants"></div>
<h1 class="abs hero-title">Making the workplace a healthier place</h1>
<p class="abs hero-sub">To provide on-sitewellness services to employers that simplify and streamline employee preventative health.</p>
<a class="abs btn btn-purple hero-btn" href="#">Get Started <svg width="13" height="13" viewBox="0 0 14 14"><circle cx="7" cy="7" r="7" fill="#fff"/><path d="M5.5 4l3 3-3 3" fill="none" stroke="#a0479c" stroke-width="2"/></svg></a>
<svg class="abs hero-edge" viewBox="0 0 1200 72" preserveAspectRatio="none">
  <polygon points="0,72 0,70 282,6 600,70 887,6 1200,70 1200,72" fill="#fff"/>
  <polygon points="74,64 282,18 490,64 282,34" fill="#0d4fa8"/>
  <polygon points="678,64 887,18 1095,64 887,34" fill="#0d4fa8"/>
</svg>

<!-- services -->
<h2 class="abs section-title" style="top:908px">Our <span>Services</span></h2>
<svg class="abs title-line" style="left:576px;top:956px" viewBox="0 0 46 10"><circle cx="5" cy="5" r="3.5" fill="none" stroke="#a0479c" stroke-width="2"/><line x1="9" y1="5" x2="46" y2="5" stroke="#a0479c" stroke-width="2"/></svg>

<span class="abs arrow" style="left:50px;top:1157px">&#8249;</span>
<span class="abs arrow" style="left:1134px;top:1157px">&#8250;</span>

<article class="abs service-card" style="left:96px;width:322px">
  <div class="service-photo" role="img" aria-label="Nurse giving a vaccine shot to a masked patient" style="background:linear-gradient(135deg,#6b5a52,#a98f7f 45%,#d8d2cc)"></div>
  <div class="abs service-icon" style="left:125px;top:185px"><i></i></div>
  <h3 class="abs service-label" style="left:0;top:266px">Covid booster</h3>
</article>

<article class="abs service-card service-featured" style="left:432px;width:323px">
  <div class="service-icon" style="margin:34px auto 0"><i></i></div>
  <h3 style="font-size:17px;font-weight:700;margin:12px 0 16px">Pneumonia vaccines</h3>
  <p>Ensure your employees and their families remain healthy this flu season. Host a flu shot clinic on site to help your employees get vaccinated.</p>
  <a class="learn-small" href="#" style="margin:18px auto 0">LEARN MORE <svg width="11" height="11" viewBox="0 0 14 14"><circle cx="7" cy="7" r="7" fill="#0d4fa8"/><path d="M5.5 4l3 3-3 3" fill="none" stroke="#fff" stroke-width="2"/></svg></a>
</article>

<article class="abs service-card" style="left:769px;width:323px">
  <div class="service-photo" role="img" aria-label="Doctor reviewing a clipboard with a patient during a wellness screening" style="background:linear-gradient(135deg,#e9e3dc,#c9beb2 50%,#8b7d70)"></div>
  <div class="abs service-icon" style="left:125px;top:185px"><i></i></div>
  <h3 class="abs service-label" style="left:0;top:266px">wellness screenings</h3>
</article>

<!-- about -->
<div class="abs about-bg"></div>
<h2 class="abs about-title">About <span>Us</span></h2>
<svg class="abs title-line" style="left:109px;top:1544px" viewBox="0 0 46 10"><circle cx="5" cy="5" r="3.5" fill="none" stroke="#a0479c" stroke-width="2"/><line x1="9" y1="5" x2="46" y2="5" stroke="#a0479c" stroke-width="2"/></svg>
<p class="abs about-text">Vitality Caravan, PLLC mission: Making the workplace a healthier place. To provide on-sitewellness services to employers that simplify and streamline employee preventative health. Pharmacist owned and operated. Vitality Caravan, PLLC was started by local, Washington state licensed pharmacist with over 15 years experience vaccinating patients. She is a highly skilled immunizer and enjoys interacting with patients while providing this important preventative health services. Her vaccination experience spans from individual patient vaccinations to large clinics during community outbreaks.</p>
<a class="abs btn btn-purple" href="#" style="left:110px;top:1877px;width:173px;height:50px">Learn More <svg width="13" height="13" viewBox="0 0 14 14"><circle cx="7" cy="7" r="7" fill="#fff"/><path d="M5.5 4l3 3-3 3" fill="none" stroke="#a0479c" stroke-width="2"/></svg></a>
<a class="abs btn btn-blue" href="#" style="left:299px;top:1877px;width:197px;height:50px">Schedule Today <svg width="13" height="13" viewBox="0 0 14 14"><circle cx="7" cy="7" r="7" fill="#fff"/><path d="M5.5 4l3 3-3 3" fill="none" stroke="#0d4fa8" stroke-width="2"/></svg></a>
<div class="abs dots"></div>
<svg class="abs" style="left:750px;top:1660px" width="351" height="301" viewBox="0 0 351 301"><polygon points="351,0 351,301 0,301 351,0" fill="#0d4fa8"/></svg>
<div class="abs about-photo" role="img" aria-label="Businessman with a tablet talking with a doctor in a white coat"></div>

<!-- cta -->
<section class="abs cta"></section>
<h2 class="abs cta-title">Reserve your on-site mobile vaccine<br>clinic today!</h2>
<svg class="abs title-line" style="left:576px;top:2182px" viewBox="0 0 46 10"><circle cx="5" cy="5" r="3.5" fill="none" stroke="#fff" stroke-width="2"/><line x1="9" y1="5" x2="46" y2="5" stroke="#fff" stroke-width="2"/></svg>
<a class="abs btn btn-purple cta-btn" href="#">Calendar <svg width="14" height="14" viewBox="0 0 14 14"><rect x="1" y="2" width="12" height="11" rx="1" fill="none" stroke="#fff" stroke-width="1.6"/><line x1="1" y1="5.5" x2="13" y2="5.5" stroke="#fff" stroke-width="1.6"/><line x1="4" y1="0" x2="4" y2="3" stroke="#fff" stroke-width="1.6"/><line x1="10" y1="0" x2="10" y2="3" stroke="#fff" stroke-width="1.6"/></svg></a>

<!-- pricing -->
<div class="abs pricing-bg" role="img" aria-label="Faint background of a workplace health consultation"></div>
<h2 class="abs section-title" style="top:2417px">Our <span>Pricing</span></h2>
<svg class="abs title-line" style="left:579px;top:2463px" viewBox="0 0 46 10"><circle cx="5" cy="5" r="3.5" fill="none" stroke="#a0479c" stroke-width="2"/><line x1="9" y1="5" x2="46" y2="5" stroke="#a0479c" stroke-width="2"/></svg>

<article class="abs price-card" style="left:171px">
  <h3 class="step">Step 1</h3>
  <div class="step-icon" role="img" aria-label="Meditating person icon"></div>
  <p class="step-desc">Submit Vaccine Clinic Needs Questionnaire</p>
  <div class="step-rule"></div>
  <ul class="ticks">
    <li><svg class="tick" viewBox="0 0 12 12"><circle cx="6" cy="6" r="6" fill="#0d4fa8"/><path d="M3.3 6.2l1.8 1.8 3.6-3.6" fill="none" stroke="#fff" stroke-width="1.5"/></svg>Lorem ipsum dolor sit amet</li>
    <li><svg class="tick" viewBox="0 0 12 12"><circle cx="6" cy="6" r="6" fill="#0d4fa8"/><path d="M3.3 6.2l1.8 1.8 3.6-3.6" fill="none" stroke="#fff" stroke-width="1.5"/></svg>Lorem ipsum dolor sit amet</li>
    <li><svg class="tick" viewBox="0 0 12 12"><circle cx="6" cy="6" r="6" fill="#0d4fa8"/><path d="M3.3 6.2l1.8 1.8 3.6-3.6" fill="none" stroke="#fff" stroke-width="1.5"/></svg>Lorem ipsum dolor sit amet</li>
  </ul>
</article>

<article class="abs price-card featured" style="left:467px">
  <h3 class="step">Step 2</h3>
  <div class="step-icon" role="img" aria-label="Hands holding a medical cross icon"></div>
  <p class="step-desc">Vitality Caravan, PLLC will contact you to schedule on-site vaccine clinic.</p>
  <div class="step-rule"></div>
  <ul class="ticks">
    <li><svg class="tick" viewBox="0 0 12 12"><circle cx="6" cy="6" r="6" fill="#0d4fa8"/><path d="M3.3 6.2l1.8 1.8 3.6-3.6" fill="none" stroke="#fff" stroke-width="1.5"/></svg>Lorem ipsum dolor sit amet</li>
    <li><svg class="tick" viewBox="0 0 12 12"><circle cx="6" cy="6" r="6" fill="#0d4fa8"/><path d="M3.3 6.2l1.8 1.8 3.6-3.6" fill="none" stroke="#fff" stroke-width="1.5"/></svg>Lorem ipsum dolor sit amet</li>
  </ul>
</article>

<article class="abs price-card" style="left:764px">
  <h3 class="step">Step 3</h3>
  <div class="step-icon" role="img" aria-label="Vaccine vial and syringe icon"></div>
  <p class="step-desc">Submit Vaccine Clinic Needs Questionnaire</p>
  <div class="step-rule"></div>
  <ul class="ticks">
    <li><svg class="tick" viewBox="0 0 12 12"><circle cx="6" cy="6" r="6" fill="#0d4fa8"/><path d="M3.3 6.2l1.8 1.8 3.6-3.6" fill="none" stroke="#fff" stroke-width="1.5"/></svg>Lorem ipsum dolor sit amet</li>
    <li><svg class="tick" viewBox="0 0 12 12"><circle cx="6" cy="6" r="6" fill="#0d4fa8"/><path d="M3.3 6.2l1.8 1.8 3.6-3.6" fill="none" stroke="#fff" stroke-width="1.5"/></svg>Lorem ipsum dolor sit amet</li>
    <li><svg class="tick" viewBox="0 0 12 12"><circle cx="6" cy="6" r="6" fill="#0d4fa8"/><path d="M3.3 6.2l1.8 1.8 3.6-3.6" fill="none" stroke="#fff" stroke-width="1.5"/></svg>Lorem ipsum dolor sit amet</li>
  </ul>
</article>

<!-- footer -->
<footer class="abs footer"></footer>
<svg class="abs footer-edge" viewBox="0 0 1200 82" preserveAspectRatio="none">
  <polygon points="0,0 1200,0 1200,15 890,78 600,10 300,78 0,15" fill="#eceef1"/>
  <polygon points="79,22 285,52 495,22 285,40" fill="#0d4fa8"/>
  <polygon points="682,22 890,52 1100,22 890,40" fill="#0d4fa8"/>
</svg>

<a class="abs brand footer-brand" href="#"><span class="brand-mark"></span>Vitality Caravan</a>
<div class="abs footer-contact" style="top:3190px"><svg width="12" height="12" viewBox="0 0 12 12"><path d="M2 0.5l2.3 2.3-1.2 1.6a7 7 0 0 0 4.5 4.5l1.6-1.2 2.3 2.3-1.6 1.6C5 11.5.5 7 .4 2.1z" fill="#fff"/></svg>+1 555 010 2040</div>
<div class="abs footer-contact" style="top:3233px"><svg width="13" height="10" viewBox="0 0 13 10"><rect width="13" height="10" rx="1" fill="#fff"/><path d="M0.5 1l6 4.5 6-4.5" fill="none" stroke="#000" stroke-width="1.2"/></svg>info@vitalitycaravan.example</div>

<div class="abs" style="left:410px;top:3083px">
  <h4 class="footer-head">Quick links</h4>
  <ul class="footer-links" style="margin-top:20px"><li>Home</li><li>About Us</li><li>Services</li><li>Pricing</li><li>Contact Us</li></ul>
</div>
<div class="abs" style="left:586px;top:3083px">
  <h4 class="footer-head">Help</h4>
  <ul class="footer-links" style="margin-top:20px"><li>FAQ</li><li>Privacy Policy</li><li>Support</li><li>Terms &amp; Condition</li><li>Site Map</li></ul>
</div>
<h4 class="abs footer-head" style="left:792px;top:3083px">Subscribe for Updates</h4>
<p class="abs newsletter" style="top:3118px">Subscribe to our Newsletter to receive updates, access to exclusive deals, &amp; more.</p>
<div class="abs subscribe"><span>Emaill Address</span><b>SIGN UP</b></div>
<div class="abs social">Contact With Us:<i></i><i></i><i></i><i></i></div>
<div class="abs footer-rule"></div>
<p class="abs copyright">© 2022 Copyrights Vitality Caravan LLC &nbsp;All Rights Reserved.</p>

</body>
</html>
```